cryotherapy business . Whole Body Cryotherapy, Localised Cryotherapy, Cryofacials

Need home page plus services, about, pricing, online booking, contact and blog page

I want something slick, hip and professional. Our studio colours are duck egg blue, white and grey

I would also like a social media scroll at the bottom of every page

I will upload some web designs that I like the look of

Target Market(s)

Men and Women 25-45

Industry/Entity Type

Health And Wellness

Coding

Coded - Design and coding required

Number of Pages Required

5+ page

Font styles to use
Serif
Sans Serif

Requirements
Must have
• Must be eye catching and easy to navigate
Nice to have
• animation
Should not have
• Not sure what the site should not have. I am fairly open to ideas as this is a brand new business.

```html
<!DOCTYPE html>
<html lang="en">
<head>
<meta charset="utf-8">
<title>Frostline – Whole Body, Localised &amp; Cryofacials</title>
<link href="https://fonts.googleapis.com/css2?family=Roboto:wght@300;400&display=swap" rel="stylesheet">
<style>
:root{
  --duck:#a8cdd5;
  --duck-text:#9ccad3;
  --duck-deep:#7fb0b5;
  --ink:#3a3f44;
  --body:#444;
  --line:#dcdcdc;
  --page:#fafafa;
  --white:#fff;
  --dark-btn:#3c4246;
}
*{box-sizing:border-box;margin:0;padding:0}
html,body{width:890px;height:1200px;overflow:hidden}
body{background:var(--page);font-family:'Roboto',sans-serif;font-weight:300;color:var(--body);position:relative}
.abs{position:absolute}
.top-rule{left:0;top:0;width:890px;height:3px;background:var(--duck)}
.brand{left:62px;top:19px;display:flex;align-items:center;gap:8px}
.brand .mark{width:30px;height:30px;border:1.5px solid var(--duck-text);border-radius:50%}
.brand .name{font-size:21px;font-weight:300;color:var(--duck-text);letter-spacing:1px;line-height:1}
.brand .tag{font-size:6.5px;font-weight:400;color:var(--ink);letter-spacing:1.2px;margin-top:3px}
.nav{right:62px;top:25px;display:flex;gap:15px;font-size:10.5px;color:var(--ink);font-weight:300}
.nav .active{color:var(--duck-text)}
.header-rule{left:62px;top:66px;width:766px;height:1px;background:var(--line)}
.hero-title{left:62px;top:108px;font-size:17px;color:var(--duck-text)}
.hero-text{left:62px;top:149px;font-size:10px;line-height:13.7px;color:var(--ink)}
.pill{top:198px;width:128px;height:25px;border:1px solid var(--duck-text);border-radius:13px;color:var(--duck-text);font-size:13.5px;display:flex;align-items:center;justify-content:center}
.about-band{left:0;top:284px;width:890px;height:256px;background:var(--duck)}
.about-photo{left:0;top:284px;width:330px;height:256px;background:linear-gradient(90deg,#8fa8c0 0%,#a9bccd 45%,rgba(168,205,213,0) 100%)}
.about-title{left:189px;top:318px;font-size:16.5px;color:var(--white)}
.about-text{left:189px;top:357px;width:385px;font-size:9.7px;line-height:13.7px;color:var(--white)}
.about-text p+p{margin-top:13.7px}
.booking{left:619px;top:104px;width:209px;height:323px;background:var(--white);border:1px solid #8a8f93;border-radius:3px}
.booking .badge{position:absolute;left:79px;top:-25px;width:50px;height:50px;border-radius:50%;background:var(--white);border:1px solid #777;display:flex;align-items:center;justify-content:center}
.booking .badge span{width:24px;height:24px;border-radius:50%;border:1.5px solid var(--duck-text)}
.booking h2{position:absolute;left:0;width:100%;top:35px;text-align:center;font-size:11.5px;font-weight:300;color:var(--duck-text)}
.field{position:absolute;left:16px;width:177px}
.field label{display:block;font-size:6.5px;color:var(--ink);font-weight:400;height:8px}
.field .input{margin-top:6px;height:17px;border:1px solid var(--duck);border-radius:2px;background:#fafcfc}
.book-btn{position:absolute;left:16px;top:284px;width:177px;height:17px;background:var(--duck);border-radius:2px;color:var(--white);font-size:8px;display:flex;align-items:center;justify-content:center}
.card{top:608px;width:224px;height:327px;background:var(--white);border:1px solid #cfe2e6;border-radius:6px}
.card .thumb{position:absolute;left:6px;top:6px;width:211px;height:145px}
.card h3{position:absolute;left:0;width:100%;top:166px;text-align:center;font-size:15px;line-height:20.5px;font-weight:300;color:var(--duck-text)}
.card p{position:absolute;left:26px;top:221px;width:176px;font-size:8px;line-height:11.4px;color:var(--ink)}
.card .more{position:absolute;left:145px;top:284px;width:60px;height:17px;background:var(--dark-btn);color:var(--white);font-size:8px;display:flex;align-items:center;justify-content:center}
.card .more.hover{background:var(--duck)}
.footer{left:0;top:1002px;width:890px;height:161px;background:linear-gradient(90deg,var(--duck-deep),#a7cdd4)}
.foot-brand{left:62px;top:1033px;width:140px;text-align:center;color:var(--white)}
.foot-brand .mark{width:56px;height:56px;border:2px solid var(--white);border-radius:50%;margin:0 auto 6px}
.foot-brand .name{font-size:19px;letter-spacing:1px;line-height:1}
.foot-brand .tag{font-size:6px;font-weight:400;letter-spacing:1px;margin-top:2px}
.vrule{top:1022px;width:1px;height:121px;background:rgba(255,255,255,.45)}
.foot-head{top:1034px;font-size:10px;color:var(--white);letter-spacing:.3px}
.contacts{left:322px;top:1064px;font-size:8.3px;line-height:13.8px;color:var(--white)}
.contacts li{list-style:none;display:flex;gap:7px}
.contacts svg{width:9px;height:9px;margin-top:2px;flex:none}
.contacts .pad{padding-left:16px}
.links{left:532px;top:1064px;font-size:8.3px;line-height:12.7px;color:var(--white);list-style:none}
.links li::before{content:"» ";font-size:7px}
.follow{left:705px;top:1083px;font-size:10px;color:var(--white)}
.socials{left:705px;top:1101px;display:flex;gap:4px}
.socials span{width:21px;height:21px;border-radius:50%;background:var(--white)}
.copyright{left:0;top:1174px;width:890px;text-align:center;font-size:10px;color:var(--ink)}
</style>
</head>
<body>
<div class="abs top-rule"></div>

<header>
  <div class="abs brand">
    <span class="mark"></span>
    <div><div class="name">FROSTLINE</div><div class="tag">WHOLE BODY, LOCALISED &amp; CRYOFACIALS</div></div>
  </div>
  <nav class="abs nav">
    <span>Home</span><span>Our Services</span><span class="active">About Us</span><span>Price List</span><span>Blog</span><span>Contact Us</span>
  </nav>
  <div class="abs header-rule"></div>
</header>

<section>
  <h1 class="abs hero-title" style="font-weight:300">Whole Body Cryotherapy?</h1>
  <p class="abs hero-text">&nbsp;Lorem ipsum dolor sit amet, consectetur adipiscing elit.<br>tesque orci justo, sed auctor leo sodales et. Quisque fermentum ex mi,</p>
  <div class="abs pill" style="left:62px">READ MORE</div>
  <div class="abs pill" style="left:198px">GET START</div>
</section>

<section>
  <div class="abs about-band"></div>
  <div class="abs about-photo" role="img" aria-label="Photo of a person surrounded by cold mist"></div>
  <h2 class="abs about-title" style="font-weight:300">About&nbsp; Cryotherapy?</h2>
  <div class="abs about-text">
    <p>&nbsp;Lorem ipsum dolor sit amet, consectetur adipiscing elit. Etiam varius mauris ac fermentum maximus. Maecenas erat augue, egestas in odio id, scelerisque semper nisi. Etiam rutrum nibh metus, sed tempus enim laoreet vel. Pellentesque quis semper dolor. Vestibulum pellentesque orci justo, sed auctor leo sodales et. Quisque fermentum ex mi, eu mollis ex dignissim in. Suspendisse mattis vestibulum blan</p>
    <p>Vestibulum ante ipsum primis in faucibus orci luctus et ultrices posuere cubilia Curae; Curabitur vitae porta est. Phasellus nec eros tellus. Aliquam enim nunc, vehicula efficitur tellus sit amet, suscipit fermentum nunc. Quisque lacus est, gravida eu auctor id, mattis vitae enim. Vestibulum mollis elit non enim pretium, interdu</p>
  </div>
</section>

<form class="abs booking">
  <div class="badge"><span></span></div>
  <h2>Book Your Treatment Appointment</h2>
  <div class="field" style="top:65px"><label>First Name</label><div class="input"></div></div>
  <div class="field" style="top:102px"><label>Last Name</label><div class="input"></div></div>
  <div class="field" style="top:138px"><label>Contact Number</label><div class="input"></div></div>
  <div class="field" style="top:175px"><label>Email ID</label><div class="input"></div></div>
  <div class="field" style="top:212px"><label>City / Town</label><div class="input"></div></div>
  <div class="field" style="top:249px"><label>Treatment</label><div class="input"></div></div>
  <div class="book-btn">Book Now</div>
</form>

<section>
  <article class="abs card" style="left:89px">
    <div class="thumb" role="img" aria-label="Promotional graphic about integrated cold therapy on deep blue with white mist" style="background:linear-gradient(180deg,#0b4d9c 0%,#0f56a6 65%,#5d8fcb 100%)"></div>
    <h3>Cold Integrated<br>Cryotherapy</h3>
    <p>&nbsp;Lorem ipsum dolor sit amet, consectetur adipiscing elit. Etiam varius mauris ac fermentum maximus. Maecenas erat augue, egestas in odio id, scelerisque semper nisi. Etiam rutrum nibh metus, sed tempus enim laoreet vel.</p>
    <div class="more">Read More</div>
  </article>
  <article class="abs card" style="left:333px">
    <div class="thumb" role="img" aria-label="Photo of a localised cold treatment being applied to a client's neck" style="background:linear-gradient(135deg,#e6e8ec 0%,#d9c7bb 45%,#3f5fa6 80%,#cfd5de 100%)"></div>
    <h3>Cold Integrated<br>Cryotherapy</h3>
    <p>&nbsp;Lorem ipsum dolor sit amet, consectetur adipiscing elit. Etiam varius mauris ac fermentum maximus. Maecenas erat augue, egestas in odio id, scelerisque semper nisi. Etiam rutrum nibh metus, sed tempus enim laoreet vel.</p>
    <div class="more hover">Read More</div>
  </article>
  <article class="abs card" style="left:577px">
    <div class="thumb" role="img" aria-label="Photo of a whole body cryotherapy chamber in a treatment room" style="background:linear-gradient(90deg,#7c7872 0%,#a29b90 40%,#bdb6aa 100%)"></div>
    <h3>Cold Integrated<br>Cryotherapy</h3>
    <p>&nbsp;Lorem ipsum dolor sit amet, consectetur adipiscing elit. Etiam varius mauris ac fermentum maximus. Maecenas erat augue, egestas in odio id, scelerisque semper nisi. Etiam rutrum nibh metus, sed tempus enim laoreet vel.</p>
    <div class="more">Read More</div>
  </article>
</section>

<footer>
  <div class="abs footer"></div>
  <div class="abs foot-brand">
    <div class="mark"></div>
    <div class="name">FROSTLINE</div>
    <div class="tag">WHOLE BODY, LOCALISED &amp; CRYOFACIALS</div>
  </div>
  <div class="abs vrule" style="left:276px"></div>
  <div class="abs vrule" style="left:489px"></div>

  <div class="abs foot-head" style="left:322px">OUR CONTACTS:</div>
  <ul class="abs contacts">
    <li><svg viewBox="0 0 10 10"><path d="M5 0.5a3.3 3.3 0 0 0-3.3 3.3C1.7 6.3 5 9.5 5 9.5s3.3-3.2 3.3-5.7A3.3 3.3 0 0 0 5 0.5zm0 4.6a1.3 1.3 0 1 1 0-2.6 1.3 1.3 0 0 1 0 2.6z" fill="#cfe3e7"/></svg>48 Harbour Lane, Northfield</li>
    <li class="pad">Westland, 20418</li>
    <li><svg viewBox="0 0 10 10"><path d="M2.2 0.8l1.6 1.8-.8 1.3c.6 1.2 1.5 2.1 2.8 2.8l1.3-.8 1.8 1.6-1 1.5C4.4 8.8 1.2 5.6.7 1.8z" fill="#cfe3e7"/></svg>+00 - 123 456 7890</li>
    <li><svg viewBox="0 0 10 10"><rect x="0.5" y="2" width="9" height="6" fill="#cfe3e7"/><path d="M0.5 2l4.5 3.5L9.5 2" stroke="#8cb8bd" stroke-width=".8" fill="none"/></svg>hello@frostline-studio.com</li>
  </ul>

  <div class="abs foot-head" style="left:532px">USEFUL LINKS</div>
  <ul class="abs links">
    <li>Home</li><li>Products</li><li>Downloads</li><li>Career</li><li>Contact Us</li>
  </ul>

  <div class="abs follow">Follow us on:</div>
  <div class="abs socials"><span></span><span></span><span></span><span></span></div>
</footer>

<div class="abs copyright">Copyrights © 2014 All Rights Reserved &nbsp;| &nbsp;&nbsp; Terms of Use / Privacy Policy</div>
</body>
</html>
```